Assorted Banner Ads

Create standard sized banner ads (300x250, 728x90, 160x600) using logo and create exciting ads using collateral provided and your own ideas.

```html
<!DOCTYPE html>
<html lang="en">
<head>
<meta charset="utf-8">
<title>Sunken Chest Quest – Banner Set</title>
<link href="https://fonts.googleapis.com/css2?family=Kaushan+Script&family=Anton&family=Montserrat:wght@600;700&display=swap" rel="stylesheet">
<style>
  :root {
    --page-bg: #e4e5e7;
    --header-brown: #2a140b;
    --photo-dark: #3a1d0c;
    --photo-mid: #8a4a1c;
    --photo-warm: #c47a35;
    --wedge-light: #f4f8f5;
    --wedge-green: #6fb98a;
    --brand-green: #2f8a4f;
    --brand-text: #3a3a3a;
    --headline-yellow: #f7e21a;
    --footer-orange: #e8620c;
    --pill-yellow: #f8ea1e;
    --white: #ffffff;
    --ink: #111111;
  }
  * { box-sizing: border-box; margin: 0; padding: 0; }
  html, body { width: 1200px; height: 1200px; overflow: hidden; }
  body { background: var(--page-bg); position: relative; font-family: "Montserrat", Arial, sans-serif; }

  .banner { position: absolute; overflow: hidden; box-shadow: 0 6px 14px rgba(0,0,0,.25); }
  .banner-title { font-family: "Kaushan Script", cursive; color: var(--white); font-weight: 400; line-height: 1; }
  .photo { position: absolute; background: linear-gradient(160deg, var(--photo-warm) 0%, var(--photo-mid) 35%, var(--photo-dark) 100%); }
  .wedge { position: absolute; inset: 0; width: 100%; height: 100%; }
  .brand { position: absolute; display: flex; flex-direction: column; align-items: center; gap: 8px; }
  .brand-mark { width: 26px; height: 26px; background: var(--brand-green); }
  .brand-name { font-weight: 700; color: var(--brand-text); letter-spacing: 1px; text-align: center; line-height: 1.15; }
  .headline { position: absolute; font-family: "Anton", Impact, sans-serif; color: var(--headline-yellow); text-transform: uppercase; line-height: 1.1; letter-spacing: .5px; }
  .headline-big { position: absolute; font-family: "Anton", Impact, sans-serif; color: var(--headline-yellow); font-style: italic; text-transform: uppercase; transform: rotate(-12deg); transform-origin: left center; -webkit-text-stroke: 1.5px var(--ink); letter-spacing: 1px; }
  .footer { position: absolute; background: var(--footer-orange); }
  .phone-pill { position: absolute; background: var(--pill-yellow); border: 2px solid #b9a500; border-radius: 999px; color: var(--ink); font-weight: 700; display: flex; align-items: center; justify-content: center; }
  .site-url { position: absolute; color: var(--white); font-weight: 600; }

  /* Skyscraper 160x600 */
  .skyscraper { left: 196px; top: 36px; width: 246px; height: 920px; background: var(--header-brown); }
  .skyscraper .header { position: absolute; left: 0; top: 0; width: 100%; height: 178px; padding: 20px 0 0 40px; }
  .skyscraper .banner-title { font-size: 46px; }
  .skyscraper .photo { left: 0; top: 178px; width: 100%; height: 626px; }
  .skyscraper .brand { left: 58px; top: 350px; width: 180px; }
  .skyscraper .brand-name { font-size: 17px; }
  .skyscraper .headline { left: 16px; top: 510px; font-size: 25px; }
  .skyscraper .headline-big { left: 12px; top: 620px; font-size: 36px; }
  .skyscraper .footer { left: 0; top: 770px; width: 100%; height: 150px; }
  .skyscraper .phone-pill { left: 38px; top: 40px; width: 170px; height: 42px; font-size: 19px; }
  .skyscraper .site-url { left: 0; width: 100%; top: 105px; text-align: center; font-size: 13px; }

  /* Medium rectangle 300x250 */
  .rectangle { left: 500px; top: 498px; width: 554px; height: 458px; background: var(--header-brown); }
  .rectangle .header { position: absolute; left: 0; top: 0; width: 100%; height: 74px; padding: 14px 0 0 28px; }
  .rectangle .banner-title { font-size: 46px; }
  .rectangle .photo { left: 0; top: 74px; width: 100%; height: 330px; }
  .rectangle .brand { left: 330px; top: 192px; width: 220px; }
  .rectangle .brand-name { font-size: 20px; }
  .rectangle .headline { left: 28px; top: 200px; font-size: 30px; }
  .rectangle .headline-big { left: 20px; top: 340px; font-size: 44px; }
  .rectangle .footer { left: 0; top: 400px; width: 100%; height: 58px; }
  .rectangle .site-url { left: 14px; top: 16px; font-size: 20px; }
  .rectangle .phone-pill { left: 345px; top: 6px; width: 200px; height: 46px; font-size: 22px; }

  /* Leaderboard 728x90 */
  .leaderboard { left: 49px; top: 1003px; width: 1102px; height: 136px; background: var(--header-brown); }
  .leaderboard .header { position: absolute; left: 0; top: 0; width: 206px; height: 100%; padding: 10px 0 0 44px; }
  .leaderboard .banner-title { font-size: 36px; }
  .leaderboard .photo { left: 206px; top: 0; width: 654px; height: 100%; }
  .leaderboard .brand { left: 640px; top: 14px; width: 220px; gap: 6px; }
  .leaderboard .brand-name { font-size: 18px; }
  .leaderboard .headline { left: 230px; top: 12px; font-size: 27px; }
  .leaderboard .headline-big { left: 246px; top: 96px; font-size: 38px; }
  .leaderboard .footer { left: 860px; top: 0; width: 242px; height: 100%; }
  .leaderboard .phone-pill { left: 36px; top: 42px; width: 166px; height: 40px; font-size: 19px; }
  .leaderboard .site-url { left: 0; width: 100%; top: 110px; text-align: center; font-size: 13px; }
</style>
</head>
<body>

  <section class="banner skyscraper" aria-label="Skyscraper banner">
    <div class="header"><h2 class="banner-title">Sunken<br>Chest<br>Quest</h2></div>
    <div class="photo" role="img" aria-label="Photo of a wooden pirate ship cabin escape room interior">
      <svg class="wedge" viewBox="0 0 246 626" preserveAspectRatio="none" aria-hidden="true">
        <defs><linearGradient id="wedge-sky" x1="0" y1="0" x2="1" y2="0"><stop offset="0" stop-color="var(--wedge-green)"/><stop offset=".55" stop-color="var(--wedge-light)"/></linearGradient></defs>
        <path d="M0 212 Q150 120 246 0 L246 400 Q150 330 0 212 Z" fill="url(#wedge-sky)"/>
      </svg>
    </div>
    <div class="brand"><span class="brand-mark"></span><span class="brand-name">HARBOR LOCK<br>ESCAPES</span></div>
    <p class="headline">Can you<br>escape in</p>
    <p class="headline-big">60 Minutes?</p>
    <div class="footer">
      <div class="phone-pill">555.010.2468</div>
      <div class="site-url">HARBORLOCKESCAPES.COM</div>
    </div>
  </section>

  <section class="banner rectangle" aria-label="Medium rectangle banner">
    <div class="header"><h2 class="banner-title">Sunken Chest Quest</h2></div>
    <div class="photo" role="img" aria-label="Photo of a wooden pirate ship cabin escape room interior">
      <svg class="wedge" viewBox="0 0 554 330" preserveAspectRatio="none" aria-hidden="true">
        <defs><linearGradient id="wedge-rect" x1="0" y1="0" x2="1" y2="0"><stop offset="0" stop-color="var(--wedge-green)"/><stop offset=".6" stop-color="var(--wedge-light)"/></linearGradient></defs>
        <path d="M28 246 Q320 150 554 0 L554 330 L330 330 Q180 290 28 246 Z" fill="url(#wedge-rect)"/>
      </svg>
    </div>
    <div class="brand"><span class="brand-mark"></span><span class="brand-name">HARBOR LOCK<br>ESCAPES</span></div>
    <p class="headline">Can you<br>escape in</p>
    <p class="headline-big">60 Minutes?</p>
    <div class="footer">
      <div class="site-url">HARBORLOCKESCAPES.COM</div>
      <div class="phone-pill">555.010.2468</div>
    </div>
  </section>

  <section class="banner leaderboard" aria-label="Leaderboard banner">
    <div class="header"><h2 class="banner-title">Sunken<br>Chest<br>Quest</h2></div>
    <div class="photo" role="img" aria-label="Photo of a wooden pirate ship cabin escape room interior">
      <svg class="wedge" viewBox="0 0 654 136" preserveAspectRatio="none" aria-hidden="true">
        <defs><linearGradient id="wedge-leader" x1="0" y1="0" x2="1" y2="0"><stop offset="0" stop-color="var(--wedge-green)"/><stop offset=".7" stop-color="var(--wedge-light)"/></linearGradient></defs>
        <path d="M260 88 Q380 50 430 0 L654 0 L654 136 L430 136 Q380 110 260 88 Z" fill="url(#wedge-leader)"/>
      </svg>
    </div>
    <div class="brand"><span class="brand-mark"></span><span class="brand-name">HARBOR LOCK<br>ESCAPES</span></div>
    <p class="headline">Can you escape in</p>
    <p class="headline-big">60 Minutes?</p>
    <div class="footer">
      <div class="phone-pill">555.010.2468</div>
      <div class="site-url">HARBORLOCKESCAPES.COM</div>
    </div>
  </section>

</body>
</html>
```